Cradlecraft by Lorna Business Card Design

i am starting a new business as a reborn artist (that is painting dolls to make them look like real live babies)

i eventually want to sell the dolls that i make and have classed in reborning. but at the moment i just want to get my name out there.

I do not currently have images of the dolls so cannot have an image in the design.

Non compulsory thoughts: i like the look of old wood, white and baby pink,even hot pink, and lace, denim. i had in mind something like a tiny baby in a old cradle or something, a old drawer, box, something different or unusual, it has to be a girl baby. i am also open to other thoughts on the matter. i would like plain writing not all swirly
Updates

Sorry to change but would like it to read country cradlecraft by lorna.

Industry/Entity Type

Painting

Contact Information for Business Card

Cradlecraft by Lorna
country babies that never grow up
Reborn Artist Lorna Whitby
0431 756 842
marlo.t@quillbox.com

```html
<!DOCTYPE html>
<html lang="en">
<head>
<meta charset="utf-8">
<title>Country Cradlecraft by Lorna – Business Card</title>
<link rel="stylesheet" href="https://fonts.googleapis.com/css2?family=Arimo:wght@400;700&display=swap">
<style>
  :root {
    --cream: #fbf1d6;
    --cream-warm: #f8e4d0;
    --rose: #e8566f;
    --rose-soft: #ee7a8d;
    --white: #ffffff;
    --ring: #efe6cc;
  }
  html, body {
    margin: 0;
    padding: 0;
    width: 1200px;
    height: 740px;
    overflow: hidden;
    background: var(--cream);
  }
  .card {
    position: relative;
    width: 1200px;
    height: 740px;
    font-family: "Arimo", Arial, sans-serif;
    overflow: hidden;
  }
  .stripe-field {
    position: absolute;
    inset: 0;
    background: linear-gradient(180deg, var(--cream) 0%, var(--cream-warm) 100%);
  }
  .brand-disc {
    position: absolute;
    left: 388px;
    top: 84px;
    width: 412px;
    height: 412px;
    border-radius: 50%;
    background: var(--white);
    border: 3px solid var(--ring);
    display: flex;
    flex-direction: column;
    align-items: center;
    justify-content: center;
    color: var(--rose);
    font-weight: 700;
    text-align: center;
    line-height: 1.15;
  }
  .brand-line { font-size: 34px; }
  .brand-line--main { font-size: 44px; }
  .brand-tagline {
    margin-top: 18px;
    font-size: 19px;
    font-weight: 400;
    letter-spacing: 0.4px;
  }
  .lace-edge {
    position: absolute;
    left: 0;
    top: 550px;
    width: 1200px;
    height: 24px;
    background: linear-gradient(180deg, var(--rose-soft) 0%, var(--rose) 100%);
  }
  .contact-band {
    position: absolute;
    left: 0;
    top: 574px;
    width: 1200px;
    height: 144px;
    background: var(--rose);
    color: var(--white);
  }
  .person {
    position: absolute;
    left: 81px;
    top: 34px;
  }
  .person-name {
    margin: 0;
    font-size: 43px;
    font-weight: 700;
    letter-spacing: 0.5px;
    line-height: 1;
  }
  .person-role {
    margin: 10px 0 0;
    font-size: 26px;
    font-weight: 400;
    letter-spacing: 0.5px;
    line-height: 1;
  }
  .contact {
    position: absolute;
    right: 81px;
    top: 38px;
    text-align: right;
    font-size: 26px;
    letter-spacing: 0.8px;
    line-height: 1;
  }
  .contact p { margin: 0 0 12px; }
</style>
</head>
<body>
<main class="card">
  <div class="stripe-field" role="img" aria-label="Cream background with a pink pinstripe pattern"></div>

  <div class="brand-disc">
    <span class="brand-line">country</span>
    <span class="brand-line brand-line--main">cradlecraft</span>
    <span class="brand-line">by lorna</span>
    <span class="brand-tagline">country babies that never grow up</span>
  </div>

  <div class="lace-edge" role="img" aria-label="Pink scalloped lace edging along the top of the contact band"></div>

  <section class="contact-band">
    <div class="person">
      <h1 class="person-name">Lorna Whitby</h1>
      <p class="person-role">Reborn Artist</p>
    </div>
    <div class="contact">
      <p class="contact-phone">0431 756 842</p>
      <p class="contact-email">marlo.t@quillbox.com</p>
    </div>
  </section>
</main>
</body>
</html>
```